Leadership Development Pathways - A Poster for Leadership Development Programme

We need an image that shows how the elements of a leadership programme work together to create a whole and flowing programme. This will be used to summarise the journey that the managers attending will embark on together. The idea is that the the pathways are rooted or grounded in Purpose and Strategy. They are parallel paths and together they lead to Leadership Success.
The design has to fit with the style of other materials, so please look at the attachments. It can be more colourful that those though.
I like the hand-drawn style and organic look rather than cartoon/ powerpoint look.

Target Market(s)

Managers attending leadership development programmes

Industry/Entity Type

Leadership

Requirements
Must have
• I like the hand-drawn effect - that fits with the style of the other materials I attached to the brief.
• It needs to be "organic" looking - it's a "pathway" not a highway/ road.
• The writing needs to stand out and be easily read
Should not have
• Power-pointy look

```html
<!DOCTYPE html>
<html lang="en">
<head>
<meta charset="utf-8">
<title>Leadership Development Pathways</title>
<link href="https://fonts.googleapis.com/css2?family=Tinos:wght@400;700&display=swap" rel="stylesheet">
<style>
  :root {
    --sky-top: #3d4f6a;
    --sky-mid: #3f78b4;
    --sky-low: #6e9fd6;
    --grass: #3f7a2a;
    --grass-dark: #2d5e1d;
    --navy: #05062a;
    --orange: #f7a03a;
    --forest: #3b5a1c;
    --crimson: #9c0f1e;
    --white: #ffffff;
    --path: rgba(232, 240, 250, 0.72);
    --path-soft: rgba(245, 249, 255, 0.35);
  }
  * { box-sizing: border-box; margin: 0; padding: 0; }
  html, body { width: 1200px; height: 1200px; overflow: hidden; }
  body { font-family: "Tinos", "Times New Roman", serif; background: var(--sky-mid); }
  .poster { position: relative; width: 1200px; height: 1200px; overflow: hidden; }
  .backdrop {
    position: absolute; inset: 0;
    background:
      radial-gradient(ellipse 420px 260px at 620px 250px, rgba(240,180,110,0.85), rgba(240,180,110,0) 70%),
      linear-gradient(180deg, var(--sky-top) 0%, #5b6f80 14%, #7b8a8a 24%, var(--sky-mid) 48%, var(--sky-low) 84%, var(--sky-low) 87%);
  }
  .backdrop-land {
    position: absolute; left: 0; right: 0; top: 0; height: 480px;
    background: linear-gradient(180deg, rgba(20,30,20,0.55) 0%, rgba(30,45,30,0.35) 50%, rgba(60,90,120,0) 100%);
  }
  .backdrop-field {
    position: absolute; left: 0; right: 0; top: 1048px; bottom: 0;
    background: linear-gradient(180deg, var(--grass) 0%, var(--grass-dark) 100%);
  }
  .artwork { position: absolute; inset: 0; }
  .node {
    position: absolute; border-radius: 50%;
    display: flex; align-items: center; justify-content: center; text-align: center;
    color: var(--white); font-weight: 700; line-height: 1.3;
  }
  .node--step { font-size: 14px; padding: 10px; }
  .node--step.node--lead { font-size: 17px; }
  .node--goal { font-size: 35px; line-height: 1.25; }
  .node--root { font-size: 30px; line-height: 1.28; }
  .track-label {
    position: absolute; color: var(--white);
    font-weight: 700; display: flex; align-items: center; justify-content: center;
    text-align: center; line-height: 1.15; letter-spacing: 0.5px;
  }
</style>
</head>
<body>
<main class="poster">
  <div class="backdrop" role="img" aria-label="Landscape photograph: trees silhouetted against a sunrise over misty hills, fading into blue sky and a green field"></div>
  <div class="backdrop-land"></div>
  <div class="backdrop-field"></div>

  <svg class="artwork" width="1200" height="1200" viewBox="0 0 1200 1200">
    <defs>
      <filter id="brush" x="-10%" y="-10%" width="120%" height="120%">
        <feTurbulence type="fractalNoise" baseFrequency="0.035" numOctaves="3" seed="4" result="noise"/>
        <feDisplacementMap in="SourceGraphic" in2="noise" scale="10" xChannelSelector="R" yChannelSelector="G"/>
      </filter>
      <filter id="inked" x="-5%" y="-5%" width="110%" height="110%">
        <feTurbulence type="fractalNoise" baseFrequency="0.06" numOctaves="2" seed="9" result="noise"/>
        <feDisplacementMap in="SourceGraphic" in2="noise" scale="4" xChannelSelector="R" yChannelSelector="G"/>
      </filter>
    </defs>

    <g class="pathway-trails" filter="url(#brush)" fill="none" stroke-linecap="round">
      <g stroke="var(--path)">
        <path d="M 390 995 C 210 930 110 800 122 620 C 132 440 250 320 410 258" stroke-width="58"/>
        <path d="M 820 990 C 1010 925 1095 790 1078 600 C 1062 430 960 320 800 258" stroke-width="58"/>
        <path d="M 584 860 C 578 720 590 560 582 360" stroke-width="22"/>
      </g>
      <g stroke="var(--path-soft)">
        <path d="M 385 1008 C 200 940 96 800 110 615 C 122 430 245 305 400 244" stroke-width="20"/>
        <path d="M 826 1003 C 1020 935 1110 790 1092 598 C 1075 420 965 305 812 244" stroke-width="20"/>
      </g>
    </g>
    <g class="pathway-arrows" filter="url(#brush)" fill="var(--path)">
      <polygon points="372,226 500,222 430,312 416,268"/>
      <polygon points="838,226 710,222 780,312 794,268"/>
      <polygon points="525,370 584,285 643,370 622,370 584,318 546,370"/>
    </g>

    <g class="node-discs" filter="url(#inked)" stroke="var(--white)">
      <circle cx="590" cy="154" r="119" fill="var(--orange)" stroke-width="5"/>
      <circle cx="166" cy="376" r="75" fill="var(--navy)" stroke-width="4"/>
      <circle cx="120" cy="621" r="75" fill="var(--navy)" stroke-width="4"/>
      <circle cx="162" cy="838" r="75" fill="var(--navy)" stroke-width="4"/>
      <circle cx="581" cy="440" r="60" fill="var(--navy)" stroke-width="4"/>
      <circle cx="586" cy="598" r="70" fill="var(--navy)" stroke-width="4"/>
      <circle cx="584" cy="758" r="60" fill="var(--navy)" stroke-width="4"/>
      <circle cx="1002" cy="376" r="75" fill="var(--navy)" stroke-width="4"/>
      <circle cx="1066" cy="590" r="75" fill="var(--navy)" stroke-width="4"/>
      <circle cx="1030" cy="838" r="75" fill="var(--navy)" stroke-width="4"/>
    </g>

    <g class="track-tags" filter="url(#inked)" fill="var(--crimson)">
      <rect x="515" y="850" width="143" height="96"/>
      <rect x="354" y="952" width="150" height="90" transform="rotate(12 429 997)"/>
      <rect x="690" y="958" width="170" height="86" transform="rotate(-15 775 1001)"/>
    </g>

    <circle class="root-disc" filter="url(#inked)" cx="597" cy="1046" r="111" fill="var(--forest)" stroke="var(--white)" stroke-width="5"/>
  </svg>

  <div class="node node--goal" style="left:468px;top:32px;width:244px;height:244px;">Purposeful<br>Leadership<br>Success</div>

  <div class="node node--step node--lead" style="left:89px;top:299px;width:154px;height:154px;">Personal<br>Development<br>Focus</div>
  <div class="node node--step" style="left:43px;top:544px;width:154px;height:154px;">Leadership<br>Choice</div>
  <div class="node node--step" style="left:85px;top:761px;width:154px;height:154px;">Growing Self<br>Awareness and<br>Self Management</div>

  <div class="node node--step" style="left:519px;top:378px;width:124px;height:124px;">Quality<br>Leadership<br>Dialogues</div>
  <div class="node node--step" style="left:514px;top:526px;width:144px;height:144px;padding:4px;">Maximizing<br>Team and Individual<br>Contributions</div>
  <div class="node node--step" style="left:522px;top:696px;width:124px;height:124px;">High<br>Performance<br>Environment</div>

  <div class="node node--step" style="left:925px;top:299px;width:154px;height:154px;">Growing<br>Strategic<br>Influence</div>
  <div class="node node--step" style="left:989px;top:513px;width:154px;height:154px;">Engaging<br>Stakeholders</div>
  <div class="node node--step" style="left:953px;top:761px;width:154px;height:154px;">Turning<br>Strategy Into<br>Work</div>

  <div class="track-label" style="left:515px;top:850px;width:143px;height:96px;font-size:16px;padding-bottom:18px;">LEADING<br>OTHERS</div>
  <div class="track-label" style="left:354px;top:952px;width:150px;height:90px;font-size:23px;transform:rotate(12deg);justify-content:flex-start;padding-left:14px;text-align:left;">LEADING<br>MYSELF</div>
  <div class="track-label" style="left:690px;top:958px;width:170px;height:86px;font-size:16px;transform:rotate(-15deg);justify-content:flex-end;padding-right:10px;">LEADING<br>ORGANIZATION</div>

  <div class="node node--root" style="left:483px;top:932px;width:228px;height:228px;">Organization<br>Purpose and<br>strategy</div>
</main>
</body>
</html>
```